Business Card for a Dental Office

The design should communicate integrity, quality and reliability. We also want the card look elegant, simple, but still stand out, different from the traditional-dental-office business card.

Industry/Entity Type

Business

```html
<!DOCTYPE html>
<html lang="en">
<head>
<meta charset="utf-8">
<title>Harlow Dental Centre – Business Card</title>
<link rel="stylesheet" href="https://fonts.googleapis.com/css2?family=Oswald:wght@700&family=Open+Sans:wght@400;600&display=swap">
<style>
  :root {
    --paper: #ffffff;
    --ink: #161616;
    --gold: #b8a82a;
    --gold-deep: #9e8f1c;
    --backdrop: #e9e7e2;
    --on-gold: #ffffff;
  }
  * { box-sizing: border-box; margin: 0; padding: 0; }
  html, body {
    width: 1200px; height: 1022px; overflow: hidden;
    background: var(--backdrop);
  }
  .card {
    position: absolute; left: 250px;
    width: 700px; height: 420px;
    border-radius: 14px; overflow: hidden;
    background: var(--paper);
    box-shadow: 0 4px 18px rgba(0,0,0,.12);
  }
  .card--front { top: 60px; }
  .card--back { top: 542px; }
  .card__art { position: absolute; inset: 0; }

  .brand-name {
    position: absolute;
    font-family: "Oswald", "Arial Narrow", sans-serif;
    font-weight: 700; color: var(--ink);
    line-height: 1; letter-spacing: 1px;
    white-space: nowrap;
  }
  .tagline {
    position: absolute;
    font-family: "Open Sans", Arial, sans-serif;
    font-weight: 600; color: var(--gold);
    white-space: nowrap;
  }
  .card--front .brand-name { left: 36px; top: 32px; font-size: 56px; }
  .card--front .tagline { left: 40px; top: 100px; font-size: 22px; letter-spacing: 3px; }

  .person { position: absolute; left: 72px; top: 286px; }
  .person__name {
    font-family: "Oswald", "Arial Narrow", sans-serif;
    font-weight: 700; font-size: 27px; color: var(--ink);
    letter-spacing: 1px; line-height: 1.1;
  }
  .person__role {
    font-family: "Open Sans", Arial, sans-serif;
    font-size: 14px; letter-spacing: 2px; color: var(--gold);
  }

  .contact {
    position: absolute; left: 392px; top: 350px;
    list-style: none;
    font-family: "Open Sans", Arial, sans-serif;
    font-size: 14px; color: var(--on-gold); line-height: 20px;
  }
  .contact li { display: flex; align-items: center; gap: 10px; }
  .contact svg { width: 11px; height: 11px; flex: none; }

  .card--back .brand-name { right: 36px; top: 158px; font-size: 44px; }
  .card--back .tagline { right: 38px; top: 216px; font-size: 17px; letter-spacing: 2px; }
</style>
</head>
<body>

<section class="card card--front" aria-label="Business card front">
  <svg class="card__art" viewBox="0 0 700 420" aria-hidden="true">
    <polygon points="378,342 700,342 700,420 338,420" fill="var(--gold)"/>
    <polyline points="322,420 368,334 556,334 556,218 606,176 700,176"
              fill="none" stroke="var(--ink)" stroke-width="6" stroke-linejoin="miter"/>
    <rect x="592" y="204" width="84" height="84" fill="var(--gold)"/>
    <rect x="0" y="296" width="50" height="34" fill="var(--gold)"/>
  </svg>

  <h1 class="brand-name">HARLOW DENTAL CENTRE</h1>
  <p class="tagline">YOUR SMILE IS YOUR GIFT TO OTHERS</p>

  <div class="person">
    <p class="person__name">EVAN MARSH</p>
    <p class="person__role">DIRECTOR</p>
  </div>

  <ul class="contact">
    <li>
      <svg viewBox="0 0 12 12"><path d="M2 1l2.5 0 1 3-1.5 1a7 7 0 0 0 3 3l1-1.5 3 1V11.5C5 11.5 .5 7 .5 1z" fill="currentColor"/></svg>
      +330 5550-1427
    </li>
    <li>
      <svg viewBox="0 0 12 12"><rect x=".5" y="2" width="11" height="8" fill="none" stroke="currentColor"/><path d="M.5 2l5.5 4.5L11.5 2" fill="none" stroke="currentColor"/></svg>
      info@harlowdentalcentre.com
    </li>
    <li>
      <svg viewBox="0 0 12 12"><circle cx="6" cy="6" r="5.3" fill="none" stroke="currentColor"/><path d="M.7 6h10.6M6 .7c-3 3-3 7.6 0 10.6M6 .7c3 3 3 7.6 0 10.6" fill="none" stroke="currentColor" stroke-width=".8"/></svg>
      www.harlowdentalcentre.com
    </li>
  </ul>
</section>

<section class="card card--back" aria-label="Business card back">
  <svg class="card__art" viewBox="0 0 700 420" aria-hidden="true">
    <polyline points="0,112 110,112 160,160 160,300 110,348 0,348"
              fill="none" stroke="var(--ink)" stroke-width="6" stroke-linejoin="miter"/>
    <rect x="36" y="188" width="90" height="90" fill="var(--gold)"/>
  </svg>
  <h2 class="brand-name">HARLOW DENTAL CENTRE</h2>
  <p class="tagline">YOUR SMILE IS YOUR GIFT TO OTHERS</p>
</section>

</body>
</html>
```